Business Card Design Project

Hi,

We need new business cards for our company Brightwell Trade Partners
www.brightwelltradepartners.example

Clean design

We will be focussing a lot on social media and online business in 2013.

All our social media channels should be included
ProLinker Group or ProLinker Company Page ,Friendwall Page,Chirpline and website

Mobile number, general telephone number,emailadress, street address etc

On the back of the card we want to promote our Clearpath Mentor Coaching Workshops (we do this via our Ticketnest page) with a place for a unique voucher code (reduction of 75 € for a coaching workshop of your choice) for every card

We would like to have our personal photo's in it.

Designs should be easy to adapt afterwards (when we hire new people - new pictures etc.)

We would like to work with Zuv as business cards service

Target Market(s)

All B2B Professionals

Industry/Entity Type

Business

Requirements
Nice to have
• QR code?

```html
<!DOCTYPE html>
<html lang="en">
<head>
<meta charset="utf-8">
<title>Brightwell Trade Partners – Business Card</title>
<link href="https://fonts.googleapis.com/css2?family=Play:wght@400;700&display=swap" rel="stylesheet">
<style>
  :root {
    --page-bg: #e6eaed;
    --card-white: #ffffff;
    --band-blue: #4aa3d6;
    --frame-blue: #3d8fcf;
    --back-blue: #62b7e6;
    --back-blue-light: #8fcdf0;
    --navy: #2f3a8e;
    --voucher-fill: #3a3f98;
    --text-dark: #444b52;
    --icon-blue: #3d8fcf;
    --photo-top: #d9dcdf;
    --photo-bottom: #b9a08e;
  }
  * { box-sizing: border-box; margin: 0; padding: 0; }
  html, body { width: 1200px; height: 960px; overflow: hidden; }
  body {
    background: var(--page-bg);
    font-family: "Play", sans-serif;
    position: relative;
  }
  .card {
    position: absolute;
    left: 210px;
    width: 780px;
    height: 440px;
    box-shadow: 0 6px 18px rgba(0,0,0,0.18);
    overflow: hidden;
  }
  /* Front */
  .card-front { top: 20px; background: var(--card-white); }
  .name-band {
    position: absolute; left: 0; top: 42px; width: 100%; height: 40px;
    background: var(--band-blue);
  }
  .portrait {
    position: absolute; left: 40px; top: 30px; width: 280px; height: 300px;
    border: 4px solid var(--frame-blue);
    background: linear-gradient(180deg, var(--photo-top) 0%, var(--photo-top) 35%, var(--photo-bottom) 100%);
  }
  .holder-name {
    position: absolute; left: 368px; top: 46px;
    color: #fff; font-size: 27px; font-weight: 400; letter-spacing: 0.3px;
  }
  .holder-title {
    position: absolute; left: 368px; top: 88px;
    color: var(--text-dark); font-size: 18px;
  }
  .contact-list {
    position: absolute; left: 368px; top: 128px; list-style: none;
  }
  .contact-list li {
    display: flex; align-items: center; height: 25px;
    font-size: 17px; color: var(--text-dark);
  }
  .contact-list .icon { width: 16px; height: 16px; margin-right: 16px; flex: none; }
  .front-brand {
    position: absolute; left: 40px; top: 350px; width: 140px;
    display: flex; align-items: center; gap: 8px;
    color: var(--frame-blue); font-size: 15px; font-weight: 700; line-height: 1.1;
  }
  .brand-dot { width: 22px; height: 22px; border-radius: 50%; background: var(--band-blue); flex: none; }
  .address {
    position: absolute; left: 200px; top: 372px;
    color: var(--text-dark); font-size: 17px;
  }
  /* Back */
  .card-back {
    top: 500px;
    background: linear-gradient(110deg, var(--back-blue) 0%, var(--back-blue) 60%, var(--back-blue-light) 100%);
  }
  .back-brand {
    position: absolute; left: 0; top: 110px; width: 100%;
    display: flex; justify-content: center; align-items: center; gap: 18px;
  }
  .back-brand .brand-dot { width: 60px; height: 60px; background: #d8eefa; }
  .back-brand-name {
    color: var(--navy); font-size: 38px; font-weight: 700; line-height: 1.05;
  }
  .voucher {
    position: absolute; left: 50%; top: 282px; transform: translateX(-50%);
    width: 420px; height: 50px; border-radius: 8px;
    background: var(--voucher-fill);
    border: 2px dashed rgba(255,255,255,0.55);
    outline: 2px solid var(--voucher-fill);
    color: #eef2ff; font-size: 27px; letter-spacing: 1px;
    display: flex; align-items: center; justify-content: center;
  }
</style>
</head>
<body>

<section class="card card-front">
  <div class="name-band"></div>
  <div class="portrait" role="img" aria-label="Portrait photo of the card holder"></div>
  <div class="holder-name">Martin Calloway</div>
  <div class="holder-title">Manager</div>

  <ul class="contact-list">
    <li>
      <svg class="icon" viewBox="0 0 16 16"><path d="M3 1h3l1 4-2 1c1 2 3 4 5 5l1-2 4 1v3c0 1-1 2-2 2C7 15 1 9 1 3c0-1 1-2 2-2z" fill="var(--icon-blue)"/></svg>
      0400 555 018
    </li>
    <li>
      <svg class="icon" viewBox="0 0 16 16"><rect x="4" y="1" width="8" height="14" rx="1.5" fill="var(--icon-blue)"/><rect x="5.5" y="3" width="5" height="8" fill="#fff"/></svg>
      0400 555 018
    </li>
    <li>
      <svg class="icon" viewBox="0 0 16 16"><rect x="1" y="3" width="14" height="10" rx="1" fill="var(--icon-blue)"/><path d="M1.5 4l6.5 5 6.5-5" stroke="#fff" stroke-width="1.5" fill="none"/></svg>
      info@brightwelltradepartners.example
    </li>
    <li>
      <svg class="icon" viewBox="0 0 16 16"><circle cx="8" cy="8" r="6.5" fill="none" stroke="var(--icon-blue)" stroke-width="1.6"/><path d="M1.5 8h13M8 1.5c-3 3-3 10 0 13M8 1.5c3 3 3 10 0 13" stroke="var(--icon-blue)" stroke-width="1.2" fill="none"/></svg>
      www.brightwelltradepartners.example
    </li>
    <li>
      <svg class="icon" viewBox="0 0 16 16"><rect x="1" y="1" width="14" height="14" rx="2" fill="var(--icon-blue)"/></svg>
      /brightwelltradepartners
    </li>
    <li>
      <svg class="icon" viewBox="0 0 16 16"><rect x="1" y="1" width="14" height="14" rx="2" fill="var(--icon-blue)"/></svg>
      @brightwelltrade
    </li>
    <li>
      <svg class="icon" viewBox="0 0 16 16"><rect x="1" y="1" width="14" height="14" rx="2" fill="var(--icon-blue)"/></svg>
      brightwell-inner-circle
    </li>
  </ul>

  <div class="front-brand">
    <span class="brand-dot"></span>
    <span>Brightwell Trade Partners</span>
  </div>
  <div class="address">Lindenlaan 14, 1830 Eikhoven (Brussels Area), Belgium</div>
</section>

<section class="card card-back">
  <div class="back-brand">
    <span class="brand-dot"></span>
    <span class="back-brand-name">Brightwell<br>Trade Partners</span>
  </div>
  <div class="voucher">voucher code</div>
</section>

</body>
</html>
```